Design & Build a WordPress Website for “Quietfern Meditation” (Australian Charity Rebrand)

We are a registered Australian charity currently known as Tavolin Meditation Australia.

We are rebranding our public identity to “Quietfern Meditation” to make the meditation practice easier to understand and more relatable for people in Australia and New Zealand.

We are looking for an experienced WordPress designer + developer to design and build a complete website that reflects:

Peace

Trust

Authentic Himalayan roots

Simplicity

Spiritual depth without being religious

Warmth, friendliness, and community feeling

This is not a corporate website. This is a meditation movement website for a non-profit organisation.

Target Market(s)

Australia and New Zealand - Age 25-65

Industry/Entity Type

Not of profit meditation organisation

Requirements
Must have
• Included in the design brief attached
Nice to have
Should not have

```html
<!DOCTYPE html>
<html lang="en">
<head>
<meta charset="utf-8">
<title>Quietfern Meditation – Tavolin Meditation Australia</title>
<link href="https://fonts.googleapis.com/css2?family=Oswald:wght@400;500&family=Nunito+Sans:wght@400;600;700&family=Quicksand:wght@500&display=swap" rel="stylesheet">
<style>
:root{
  --ink:#1f1f24;
  --body:#3a3a44;
  --muted:#6b6b76;
  --accent:#7b9be0;
  --btn:#93c394;
  --btn-text:#ffffff;
  --gold:#dcc07a;
  --sky:#dfe9f3;
  --donate:#e1f0df;
  --card:#ffffff;
}
*{box-sizing:border-box;margin:0;padding:0}
html,body{width:1200px;height:4054px;overflow:hidden}
body{position:relative;background:#fff;font-family:"Nunito Sans",sans-serif;color:var(--body)}
.abs{position:absolute}
.heading{font-family:"Oswald",sans-serif;font-weight:500;text-transform:uppercase;color:var(--ink);line-height:1.15}
.heading .accent{color:var(--accent)}
.btn{position:absolute;display:flex;align-items:center;justify-content:center;background:var(--btn);color:var(--btn-text);font-family:"Oswald",sans-serif;font-weight:400;font-size:19px;text-transform:uppercase;border-radius:30px;text-decoration:none}
.wordmark{display:flex;align-items:center;gap:12px}
.wordmark .dot{width:44px;height:44px;border-radius:50%;border:3px solid var(--accent)}
.wordmark span{font-family:"Oswald",sans-serif;font-weight:500;font-size:25px;color:var(--accent);text-transform:uppercase;letter-spacing:.5px}

.hero-bg{left:0;top:0;width:1200px;height:700px;background:
  radial-gradient(ellipse 520px 320px at 820px 240px,#d6e3f1 0%,rgba(214,227,241,0) 70%),
  radial-gradient(ellipse 600px 200px at 200px 200px,#e8eff7 0%,rgba(232,239,247,0) 70%),
  linear-gradient(#f3f7fb,#ffffff)}
.welcome-bg{left:0;top:860px;width:1200px;height:480px;background:
  radial-gradient(ellipse 700px 220px at 300px 200px,#dce8f3 0%,rgba(220,232,243,0) 70%)}
.steps-bg{left:0;top:1720px;width:1200px;height:340px;background:linear-gradient(rgba(255,255,255,0),#e6eef6 70%,#d7e4f0)}
.benefits-band{left:0;top:2060px;width:1200px;height:350px;background:var(--sky)}
.benefits-lower{left:0;top:2410px;width:1200px;height:296px;background:linear-gradient(#f1f5fa,#ffffff)}
.footer-bg{left:0;top:3860px;width:1200px;height:194px;background:linear-gradient(#ffffff,#e9f0f7)}

.site-logo{left:145px;top:50px}
.lang{top:82px;height:32px;padding:0 16px 0 6px;border-radius:18px;background:#fff;box-shadow:0 2px 6px rgba(0,0,0,.12);display:flex;align-items:center;gap:10px;font-size:10px;font-weight:700;color:var(--ink)}
.lang .flag{width:22px;height:22px;border-radius:50%}
.lang-au{left:770px}
.lang-au .flag{background:#2e4a8f}
.lang-nz{left:888px}
.lang-nz .flag{background:#5b6fa3}
.menu{left:1034px;top:84px;width:20px}
.menu i{display:block;height:3px;background:var(--ink);margin-bottom:4px;border-radius:2px}

.hero-title{left:142px;top:224px;font-size:47px}
.hero-copy{left:146px;top:305px;width:470px;font-size:15.5px;line-height:27px;color:var(--body)}
.hero-copy ul{list-style:none}
.hero-copy li{position:relative;padding-left:28px}
.hero-copy li::before{content:"";position:absolute;left:3px;top:11px;width:6px;height:6px;border-radius:50%;background:var(--ink)}
.hero-btn{left:142px;top:578px;width:189px;height:58px}
.scroll-cue{left:588px;top:592px}
.hero-art{left:655px;top:230px;width:400px;height:430px;border-radius:48% 48% 40% 40%;background:radial-gradient(circle at 50% 45%,#f0b7b0 0%,#aab6d8 45%,#d9deef 75%,rgba(217,222,239,0) 100%)}

.welcome-title{left:0;width:1200px;text-align:center;top:756px;font-size:47px}
.welcome-sub{left:0;width:1200px;text-align:center;top:820px;font-size:38px;color:var(--accent)}
.welcome-copy{left:146px;top:936px;width:389px;font-size:15.5px;line-height:27px;text-align:justify}
.welcome-btn{left:146px;top:1212px;width:205px;height:58px}
.video-frame{left:595px;top:964px;width:484px;height:353px;border:3px solid var(--gold)}
.video{left:572px;top:915px;width:484px;height:353px;background:#f5f7fa;overflow:hidden}
.video .label{position:absolute;left:0;top:54px;width:100%;text-align:center;font-family:"Quicksand",sans-serif;font-weight:500;font-size:23px;letter-spacing:2px;color:#4a5570}
.video .scene{position:absolute;left:0;top:110px;width:100%;height:243px;background:linear-gradient(#e2e8f0,#b9c7d8 55%,#e7ecf2)}
.video .play{position:absolute;left:210px;top:198px}

/* steps */
.steps-title{left:0;width:1200px;text-align:center;top:1436px;font-size:47px}
.step{width:230px;height:224px;text-align:center}
.step svg.ring{position:absolute;left:0;top:0}
.step .icon{position:absolute;left:97px;top:28px}
.step .info{position:absolute;left:45px;width:140px;top:72px}
.step h3{font-size:14px;font-weight:700;color:var(--ink);line-height:18px;text-transform:uppercase}
.step p{margin-top:4px;font-size:12.5px;line-height:16px;color:var(--muted)}
.step .num{position:absolute;left:0;width:230px;top:176px;line-height:34px;font-family:"Oswald",sans-serif;font-size:25px;color:#fff}
.step-1{left:140px;top:1550px}
.step-2{left:369px;top:1637px}
.step-3{left:598px;top:1550px}
.step-4{left:825px;top:1637px}
.steps-btn{left:498px;top:1910px;width:205px;height:57px}

.benefits-title{left:0;width:1200px;text-align:center;top:2146px;font-size:47px}
.card{top:2255px;height:315px;background:var(--card);border-radius:12px;box-shadow:0 4px 14px rgba(80,100,130,.18);text-align:center}
.card.featured::after{content:"";position:absolute;inset:8px;border:1.5px solid #ecdcb4;border-radius:8px}
.card .badge{position:absolute;left:50%;top:30px;margin-left:-36px;width:72px;height:72px;border-radius:50%;display:flex;align-items:center;justify-content:center}
.card h3{position:absolute;left:20px;right:20px;top:124px;font-size:18px;font-weight:700;color:var(--ink);line-height:28px;text-transform:uppercase}
.card p{position:absolute;left:26px;right:26px;font-size:14px;line-height:25px;color:var(--muted)}
.card a{position:absolute;left:0;right:0;bottom:40px;font-size:16px;font-weight:700;color:var(--btn);text-decoration:underline}
.card-1{left:143px;width:287px}
.card-2{left:457px;width:283px}
.card-3{left:769px;width:288px}
.card-1 .badge{background:#d5dff5}
.card-2 .badge{background:#dff0e1}
.card-3 .badge{background:#f5ebd6}
.benefits-btn{left:498px;top:2616px;width:205px;height:57px}

.community-title{left:146px;top:2800px;font-size:45px;line-height:56px}
.community-copy{left:146px;top:2934px;width:389px;font-size:15.5px;line-height:27px;text-align:justify}
.community-btn{left:148px;top:3136px;width:252px;height:58px}
.community-art{left:583px;top:2796px;width:535px;height:385px;border-radius:30px;background:linear-gradient(135deg,#eef2f6 0%,#d7e3ee 40%,#8fb5a6 70%,#eef1f4 100%);opacity:.85}

.donate{left:63px;top:3307px;width:1074px;height:281px;background:var(--donate);border-radius:22px}
.donate-title{left:146px;top:3372px;font-size:45px;line-height:56px}
.donate-copy{left:595px;top:3380px;width:470px;font-size:15.5px;line-height:27px}
.donate-btn{left:595px;top:3459px;width:189px;height:56px}

.footer-logo{left:145px;top:3685px}
.social{top:3780px;display:flex;gap:12px;left:191px}
.social i{display:block;width:32px;height:32px;border-radius:50%;border:1.5px solid var(--accent);background:#eef3fc}
.links-title{left:450px;top:3666px;font-family:"Oswald",sans-serif;font-size:21px;color:var(--ink)}
.links{top:3706px;list-style:none;font-size:15px;line-height:27px;color:var(--body)}
.links-a{left:452px}
.links-b{left:748px}
.divider{left:40px;top:3898px;width:1120px;height:1px;background:#e0e4ea}
.contact{top:3916px;display:flex;align-items:center;gap:16px;font-size:19px;color:var(--ink)}
.contact .ic{width:40px;height:40px;border-radius:50%;display:flex;align-items:center;justify-content:center}
.contact-address{left:156px}
.contact-address .ic{background:#9cc59d}
.contact-email{left:675px}
.contact-email .ic{background:#f7dede}
.copyright{left:0;width:1200px;top:4002px;text-align:center;font-size:15px;color:var(--body)}
</style>
</head>
<body>

<div class="abs hero-bg"></div>
<div class="abs welcome-bg"></div>
<div class="abs steps-bg"></div>
<div class="abs benefits-band"></div>
<div class="abs benefits-lower"></div>
<div class="abs footer-bg"></div>

<header>
  <div class="abs site-logo wordmark"><i class="dot"></i><span>Tavolin Meditation</span></div>
  <div class="abs lang lang-au"><i class="flag"></i>AUSTRALIA</div>
  <div class="abs lang lang-nz"><i class="flag"></i>NEW ZEALAND</div>
  <div class="abs menu"><i></i><i></i><i></i></div>
</header>

<section class="hero">
  <h1 class="abs heading hero-title">Quietfern <span class="accent">Meditation</span></h1>
  <div class="abs hero-copy">
    <p>Quietfern Meditation is a simple, natural meditation technique taught freely to help people experience inner peace, clarity, and emotional balance.</p>
    <p>We conduct:</p>
    <ul>
      <li>Free meditation sessions</li>
      <li>Community programs</li>
      <li>Events (International Yoga Day, group meditations, etc.)</li>
      <li>Donation drives for building a meditation centre (Shantivan project)</li>
    </ul>
  </div>
  <a class="btn hero-btn">Get Started</a>
  <svg class="abs scroll-cue" width="24" height="56" viewBox="0 0 24 56" fill="none" stroke="#333" stroke-width="1.6">
    <rect x="5" y="2" width="14" height="24" rx="7"/>
    <line x1="12" y1="8" x2="12" y2="13"/>
    <polyline points="6,32 12,38 18,32"/>
    <polyline points="6,40 12,46 18,40"/>
    <polyline points="6,48 12,54 18,48"/>
  </svg>
  <div class="abs hero-art" role="img" aria-label="Illustration of a person meditating cross-legged among soft clouds and sparkles"></div>
</section>

<section class="welcome">
  <h2 class="abs heading welcome-title">Welcome to</h2>
  <h2 class="abs heading welcome-sub">Tavolin Meditation Australia</h2>
  <p class="abs welcome-copy">Your bright, bubbly oasis of calm in the vast digital desert. Kick off your shoes, find your favourite comfy spot, and prepare to embark on a life-changing journey to improved health, wellness, and spiritual awakening, all served with a sprinkle of playfulness and a dash of joy.Feeling stressed? Tangled in the worries of life? Or maybe just curious about how to add a new, serene rhythm to your everyday life? Tavolin Meditation Australia is the place to be!</p>
  <a class="btn welcome-btn">Read More</a>
  <div class="abs video-frame"></div>
  <div class="abs video">
    <div class="label">Shree Anandmay Guruji</div>
    <div class="scene" role="img" aria-label="Photograph of a meditation teacher seated before snowy Himalayan peaks"></div>
    <svg class="play" width="62" height="62" viewBox="0 0 62 62">
      <circle cx="31" cy="31" r="29" fill="#4f86d6" stroke="#ffffff" stroke-width="3"/>
      <polygon points="25,19 25,43 44,31" fill="#ffffff"/>
    </svg>
  </div>
</section>

<section class="steps">
  <h2 class="abs heading steps-title">How it <span class="accent">works</span></h2>

  <div class="abs step step-1">
    <svg class="ring" width="230" height="224" viewBox="0 0 230 224" fill="none">
      <path d="M52 196 A110 110 0 1 1 178 196" stroke="#5b8fe0" stroke-width="2"/>
      <circle cx="52" cy="196" r="4" fill="#5b8fe0"/><circle cx="178" cy="196" r="4" fill="#5b8fe0"/>
      <circle cx="115" cy="110" r="100" fill="#fff" stroke="#dfe6f0"/>
      <path d="M40 176 Q115 158 190 176 A100 100 0 0 1 40 176 Z" fill="#5b8fe0"/>
    </svg>
    <svg class="icon" width="36" height="36" viewBox="0 0 40 40" fill="none" stroke="#333" stroke-width="1.6"><circle cx="20" cy="14" r="6"/><path d="M20 2v4M8 14h4M28 14h4M11 5l3 3M29 5l-3 3"/><path d="M10 36c0-6 4-10 10-10s10 4 10 10z"/></svg>
    <div class="info"><h3>Choose your moment</h3><p>Sed ut perspiciatis unde omnis iste natus</p></div>
    <div class="num">01</div>
  </div>

  <div class="abs step step-2">
    <svg class="ring" width="230" height="224" viewBox="0 0 230 224" fill="none">
      <path d="M52 196 A110 110 0 1 1 178 196" stroke="#d9b94c" stroke-width="2"/>
      <circle cx="52" cy="196" r="4" fill="#d9b94c"/><circle cx="178" cy="196" r="4" fill="#d9b94c"/>
      <circle cx="115" cy="110" r="100" fill="#fff" stroke="#efe6cf"/>
      <path d="M40 176 Q115 158 190 176 A100 100 0 0 1 40 176 Z" fill="#d9b94c"/>
    </svg>
    <svg class="icon" width="36" height="36" viewBox="0 0 40 40" fill="none" stroke="#333" stroke-width="1.6"><circle cx="16" cy="10" r="4"/><path d="M8 36l4-14h8l4 14M6 36h28"/><path d="M28 12c4 0 6 3 6 6h-8"/></svg>
    <div class="info"><h3>Settle in</h3><p>Sed ut perspiciatis unde omnis iste natus rerror sit</p></div>
    <div class="num">02</div>
  </div>

  <div class="abs step step-3">
    <svg class="ring" width="230" height="224" viewBox="0 0 230 224" fill="none">
      <path d="M52 196 A110 110 0 1 1 178 196" stroke="#8fd16c" stroke-width="2"/>
      <circle cx="52" cy="196" r="4" fill="#8fd16c"/><circle cx="178" cy="196" r="4" fill="#8fd16c"/>
      <circle cx="115" cy="110" r="100" fill="#fff" stroke="#8fd16c"/>
      <path d="M40 176 Q115 158 190 176 A100 100 0 0 1 40 176 Z" fill="#8fd16c"/>
    </svg>
    <svg class="icon" width="36" height="36" viewBox="0 0 40 40" fill="none" stroke="#333" stroke-width="1.6"><path d="M4 8h12c2 0 4 2 4 4v24c0-2-2-4-4-4H4zM36 8H24c-2 0-4 2-4 4v24c0-2 2-4 4-4h12z"/><path d="M8 14h8M8 19h8M24 14h8M24 19h8"/></svg>
    <div class="info"><h3>Follow the guidance</h3><p>Sed ut perspiciatis unde omnis iste natus</p></div>
    <div class="num">03</div>
  </div>

  <div class="abs step step-4">
    <svg class="ring" width="230" height="224" viewBox="0 0 230 224" fill="none">
      <path d="M52 196 A110 110 0 1 1 178 196" stroke="#d3b36a" stroke-width="2"/>
      <circle cx="52" cy="196" r="4" fill="#d3b36a"/><circle cx="178" cy="196" r="4" fill="#d3b36a"/>
      <circle cx="115" cy="110" r="100" fill="#fff" stroke="#efe6cf"/>
      <path d="M40 176 Q115 158 190 176 A100 100 0 0 1 40 176 Z" fill="#d3b36a"/>
    </svg>
    <svg class="icon" width="36" height="36" viewBox="0 0 40 40" fill="none" stroke="#333" stroke-width="1.8"><path d="M14 8L6 16l8 8"/><path d="M6 16h16c6 0 10 4 10 10v6"/></svg>
    <div class="info"><h3>Return lighter</h3><p>Sed ut perspiciatis unde omnis iste natus rerror sit</p></div>
    <div class="num">04</div>
  </div>

  <a class="btn steps-btn">Get Started</a>
</section>

<section class="benefits">
  <h2 class="abs heading benefits-title">Our <span class="accent">benefits</span></h2>

  <article class="abs card card-1">
    <div class="badge"><svg width="36" height="36" viewBox="0 0 36 36" fill="none" stroke="#5b7fd0" stroke-width="1.6"><circle cx="18" cy="11" r="5"/><path d="M8 30c0-6 4-10 10-10s10 4 10 10z"/><circle cx="18" cy="18" r="16"/></svg></div>
    <h3>Self realisation</h3>
    <p style="top:164px">Regular practice can lead to self-realization, an understanding of one's true nature</p>
    <a>READ MORE</a>
  </article>

  <article class="abs card card-2 featured">
    <div class="badge"><svg width="36" height="36" viewBox="0 0 36 36" fill="none" stroke="#5aa56a" stroke-width="1.6"><path d="M10 32v-6c-4-3-6-7-5-12 2-7 10-10 16-8 6 2 9 8 7 14l-2 2v4h-4v6"/><circle cx="18" cy="15" r="4"/></svg></div>
    <h3>Peace of mind</h3>
    <p style="top:164px">By surrendering all thoughts and emotions, practitioners often find a deep sense of peace</p>
    <a>READ MORE</a>
  </article>

  <article class="abs card card-3">
    <div class="badge"><svg width="36" height="36" viewBox="0 0 36 36" fill="none" stroke="#b8924a" stroke-width="1.6"><path d="M10 32v-6c-4-3-6-7-5-12 2-7 10-10 16-8 6 2 9 8 7 14l-2 2v4h-4v6"/><path d="M15 12h6v6h-6z"/></svg></div>
    <h3>Improved physical health</h3>
    <p style="top:190px">Regular practice can lead to self-realization, an understanding</p>
    <a>READ MORE</a>
  </article>

  <a class="btn benefits-btn">View More</a>
</section>

<section class="community">
  <h2 class="abs heading community-title">Be part of a<br><span class="accent">caring community</span></h2>
  <p class="abs community-copy">Sed ut perspiciatis unde omnis iste natus error sit voluptatem accusantium doloremque laudantium, totam rem aperiam, eaque ipsa quae ab illo inventore veritatis et quasi architecto beatae vitae dicta sunt explicabo. Nemo enim ipsam voluptatem quia voluptas sit aspernatur aut odit aut fugit, sed quia</p>
  <a class="btn community-btn">Become a Volunteer</a>
  <div class="abs community-art" role="img" aria-label="Illustration of volunteers sharing donated boxes and gifts with a child"></div>
</section>

<section>
  <div class="abs donate"></div>
  <h2 class="abs heading donate-title">What your donation<br><span class="accent">makes possible</span></h2>
  <p class="abs donate-copy">Every contribution helps create and share moments of visible support through music, storytelling, and human connection.</p>
  <a class="btn donate-btn">Donate Now</a>
</section>

<footer>
  <div class="abs footer-logo wordmark"><i class="dot"></i><span>Tavolin Meditation</span></div>
  <div class="abs social">
    <i aria-label="Social profile one"></i><i aria-label="Social profile two"></i><i aria-label="Social profile three"></i>
  </div>
  <h4 class="abs links-title">LINKS</h4>
  <ul class="abs links links-a">
    <li>Home</li>
    <li>What is Quietfern Meditation</li>
    <li>About the Organisation</li>
    <li>Meditation Sessions</li>
    <li>Events &amp; Programs</li>
  </ul>
  <ul class="abs links links-b">
    <li>Shantivan Meditation Centre Project</li>
    <li>Resources</li>
    <li>Contact Us</li>
    <li>Volunteer With Us</li>
    <li>Donate</li>
  </ul>
  <div class="abs divider"></div>
  <div class="abs contact contact-address">
    <span class="ic"><svg width="18" height="18" viewBox="0 0 18 18" fill="#fff"><path d="M9 1C5.7 1 3 3.6 3 6.8 3 11 9 17 9 17s6-6 6-10.2C15 3.6 12.3 1 9 1zm0 8.3a2.4 2.4 0 110-4.8 2.4 2.4 0 010 4.8z"/></svg></span>
    27 Willowbank Lane, Fernvale, Victoria, 3360
  </div>
  <div class="abs contact contact-email">
    <span class="ic"><svg width="18" height="14" viewBox="0 0 18 14" fill="#d98b8b"><path d="M1 1h16v12H1z"/><path d="M1 1l8 6 8-6" stroke="#fff" stroke-width="1.4" fill="none"/></svg></span>
    info@tavolinmeditation.com.au
  </div>
  <p class="abs copyright">© 2026 Companyname.All Rights Reserved &nbsp;|&nbsp; Privacy Policy &nbsp;|&nbsp; Terms of Use</p>
</footer>

</body>
</html>
```